Single Landing Page Redesign - CRO Experts Welcome!

We need our landing page redesigned. We will be giving a lot of weight to conversion optimization so be sure to redesign the landing page with conversion optimization concepts in mind.

This is the landing page that needs to be redesigned:
http://www.plankhollow.com/message_board/forum3.html

Here are some ideas that we think could increase conversions in order of priority:

- Show a screenshot of an example forum, linked to the forum's address (http://forums.quillmeadow.com/)

- Change the "Get Feedback from Users" feature to "Mobile Friendly (perhaps a picture of an iphone with a mobile version of our forum loaded in it? - mobile version isn't launched yet)

- Mention "Social Sharing" as a feature. (perhaps mention something about content going viral?)

- Additional testimonials:
"Plank Hollow has been a superb solution for RoamFjord Travel. Our customers love it-and the customization available is flexible enough to allow us to "brand" the forums so that they fit with our main site. Tech support has been outstanding, with quick & helpful responses to the questions we've had."
Darren Pellwick
www.roamfjord.com

"Very simple and easy to set up, yet so customizable. It looks like it resides right on our site."
Osvald Trunke
www.pvdrlq.com

- Additional client logo: sparrowdale lines (sparrowdale.com) - It would be better if logos are in a horizontal line in gray.

- Benefits of creating a forum (paragraph or bullet points or any other creative way): Running a forum is an excellent way of creating a community. It can be a place for people to discuss issues, share knowledge, and talk about you, your product, or your service. In the long-term, providing a way for your users to be part of a community can prove to be invaluable in terms of search engine optimization, customer satisfaction, customer/visitor retention, brand awareness, customer support, viral promotion, building trust, and creating a new revenue stream.

- Additional info that can be included, which might increase conversions (not mandatory) (can be reworded or changed as needed):
Embed your forum into an existing website in seconds!
Cloud-Based
Secure - Our forums are equipped with security features that make hackers and spammers a thing of the past.

You are welcome to implement your own ideas as well.

Nice landing pages:
http://www.trymarrowkit.com/ (I love the big, wide design.)
http://www.vexlo.com/crm/

The physical layout of the page can be changed completely. The existing text and elements of the landing page can be changed completely. None of the existing landing page has to remain the way it is. Be creative and come up with what you think looks best. The existing landing page is only an example of what we currently have.

The PSD of our logo is attached.

We look forward to seeing your mockups!

```html
<!DOCTYPE html>
<html lang="en">
<head>
<meta charset="utf-8">
<title>Plank Hollow – Forum Landing Page</title>
<link href="https://fonts.googleapis.com/css2?family=Arimo:wght@400&family=Bitter:wght@400&display=swap" rel="stylesheet">
<style>
  :root {
    --page-bg: #ffffff;
    --column-bg: #e6e6e6;
    --header-bg: #666666;
    --brand-blue: #29a9e0;
    --brand-blue-edge: #1f97cc;
    --card-head: #cccccc;
    --band-grey: #b3b3b3;
    --text-dark: #2a2a2a;
    --text-light: #ffffff;
  }
  * { margin: 0; padding: 0; box-sizing: border-box; }
  html, body { width: 1200px; height: 1000px; overflow: hidden; background: var(--page-bg); }
  body { position: relative; font-family: "Arimo", Arial, sans-serif; }

  .page { position: absolute; left: 155px; top: 0; width: 890px; height: 1000px; background: var(--column-bg); }

  .site-header { position: absolute; left: 0; top: 0; width: 890px; height: 128px; background: var(--header-bg); }
  .brand-name { position: absolute; left: 32px; top: 54px; font-family: "Bitter", Georgia, serif; font-size: 31px; letter-spacing: 1px; color: var(--text-light); font-weight: 400; line-height: 1; }

  .main-nav { position: absolute; left: 0; top: 128px; width: 890px; height: 51px; background: var(--brand-blue); }
  .main-nav ul { list-style: none; position: absolute; left: 31px; top: 17px; font-size: 14px; color: var(--text-light); display: flex; }
  .main-nav li + li::before { content: "-"; margin: 0 6px; }

  .feature-area { position: absolute; left: 0; top: 199px; width: 890px; height: 248px; background: var(--page-bg); }
  .cta-shape { position: absolute; left: 0; top: 446px; width: 890px; height: 137px; }

  .feature-card { position: absolute; width: 203px; height: 108px; }
  .feature-card h3 { height: 42px; background: var(--card-head); border-radius: 7px 7px 0 0; font-size: 16px; font-weight: 400; color: var(--text-dark); text-align: center; line-height: 44px; }
  .feature-card p { height: 66px; background: var(--brand-blue); color: var(--text-light); font-size: 14px; line-height: 17px; padding: 16px 8px 0 10px; }
  .feature-card p.indented { padding-left: 27px; }

  .headline { position: absolute; left: 0; top: 450px; width: 890px; text-align: center; font-size: 42px; font-weight: 400; color: var(--brand-blue); }

  .cta-button { position: absolute; left: 344px; top: 590px; width: 200px; height: 56px; border-radius: 10px; background: var(--brand-blue); border: 1px solid var(--brand-blue-edge); color: var(--text-light); font-size: 19px; text-align: center; line-height: 55px; text-decoration: none; }

  .divider { position: absolute; left: 17px; top: 690px; width: 855px; height: 5px; background: var(--page-bg); }

  .extras { position: absolute; left: 17px; width: 855px; }
  .extras-row { position: absolute; left: 0; width: 855px; display: flex; justify-content: space-between; padding: 0 29px; font-size: 16px; color: var(--text-light); }
  .extras-blue { top: 712px; height: 137px; background: var(--brand-blue); }
  .extras-blue .gap { position: absolute; left: 0; top: 60px; width: 855px; height: 5px; background: var(--page-bg); }
  .extras-grey { top: 848px; height: 128px; background: var(--band-grey); }
  .extras-grey .gap { position: absolute; left: 0; top: 39px; width: 855px; height: 6px; background: var(--page-bg); }
  .extras-blue .extras-row { top: 30px; }
  .extras-grey .extras-row { top: 12px; }
</style>
</head>
<body>
<div class="page">
  <header class="site-header">
    <div class="brand-name">PLANK HOLLOW</div>
  </header>
  <nav class="main-nav">
    <ul><li>HOME</li><li>FEATURES</li><li>PRICING</li><li>CONTACT</li></ul>
  </nav>

  <section class="feature-area">
    <div class="feature-card" style="left:21px;top:11px"><h3>Instand Setup</h3><p>So easy to use, you'll be up and running in a few seconds!</p></div>
    <div class="feature-card" style="left:235px;top:11px"><h3>Fully Customisable</h3><p class="indented" style="padding-left:14px">Customised the Design and features of your Forum.</p></div>
    <div class="feature-card" style="left:449px;top:11px"><h3>Public / Private</h3><p style="padding-left:13px">Let the whole world view and contribute to your forum.</p></div>
    <div class="feature-card" style="left:663px;top:11px"><h3>Monetization</h3><p style="padding-left:6px;padding-right:2px">Make Money from your Forum by adding your own advertising.</p></div>

    <div class="feature-card" style="left:20px;top:127px"><h3>White Label</h3><p class="indented">Use your own logo and domain name.</p></div>
    <div class="feature-card" style="left:235px;top:127px"><h3>Great Support</h3><p class="indented" style="padding-left:23px">Industry Leading Phone, Chat and Email Support.</p></div>
    <div class="feature-card" style="left:449px;top:127px"><h3>SEO Friendly</h3><p style="padding-left:14px">Search Engine Optimization is built into the Foundation.</p></div>
    <div class="feature-card" style="left:663px;top:127px"><h3>Moderation</h3><p style="padding-left:21px">You decide who can view and post content.</p></div>
  </section>

  <svg class="cta-shape" viewBox="0 0 890 137" aria-hidden="true">
    <polygon points="0,0 890,0 890,1 443,136 0,1" fill="#ffffff"/>
  </svg>
  <h2 class="headline">No coding skills required!</h2>
  <a class="cta-button" href="#">Create a Forum now!</a>

  <div class="divider"></div>

  <section class="extras extras-blue">
    <div class="extras-row"><span>Login with Friendloop</span><span>Use Friendloop-Style Chat</span><span>Share Files, Photos and Videos</span></div>
    <div class="gap"></div>
  </section>
  <section class="extras extras-grey">
    <div class="extras-row"><span>Annouvnce and Organise Events</span><span>Mobile Friendly</span><span>Set User Permissions</span></div>
    <div class="gap"></div>
  </section>
</div>
</body>
</html>
```